physio rehab flyer for Vela Motion please

Specification:
Flyer is to be trifold from letter size (8.5 x 11)
-----------------------This may help you:--------------------------
I would like the look of :
clean, minimalistic look with mainly blue and green
san serif font
professional
The colors I like are blue (not the blue in the logo enclosed, I want a change, but more like the blue on my website logo) and light green.
This is my website: www.velamotiongroup.ca just so you get an idea but it will be totally changed soon to a to be determined design.
I like the blue and green in file "sample 2" (enclosed)
I like the pictures in "sample 2" file enclosed
For inspiration, I like design of this brochure: http://www.qlx.ca/HarbourRestore/PatientsFamilies/Clinics_Tests/DAWL_Service/Documents/Brochure.pdf
Here's how I see the pages layout:
----[location: this should be the cover (outside, right panel of trifold)]-----
Vela Motion Logo
Integrated Injury Rehab
Evidence-based, one-on-one care to make your recovery fast and comfortable
www.velamotiongroup.ca
---------------[location: inside, left panel]----------------------------------------
Our team leaders
[portrait here]
Harriet Osei, MD, FRCPC, MSC, CIME
Physiatrist
Dr. Osei specializes in injury rehab and sports medicine. She is highly trained having received her MD and Residency in Physiatry from Wexmoor University. Her passion is to help injured people get back to their life.
[portrait here]
Dorothy Varga, PT
Physiotherapist
Dorothy has over 10 years of experience as a Physiotherapist (5 in Canada). She has advanced training in orthopedics and manual therapy. She loves and relates well with people from the youngest to the most senior.
--------------------[location: inside, middle panel]-------------------------------
Our services
We provide integrated assessment and care from interprofessional team of regulated healthcare professionals with proven experience in injury rehabilitation:
physiatrists
sport medicine physicians
physiotherapists
chiropractors
massage therapists
acupuncturists
psychologists
We provide custom medical bracing, orthotics, orthopedic shoes, assistive devices, and medical stockings, all in one place.
----------------------[location: inside, right panel]-----------------------------------
Only registered physiotherapists
We strongly believe in consistency with your treatment plan. This means that you spend your time here one-on-one with your physiotherapist, not any students or assistants. You get consistent high quality care from a professional.
One-on-one attention
We book maximum 3 people per hour to ensure everyone gets adequate one-on-one time with their physiotherapist. This compares favorably with other clinics, who may book upwards of 5-6 per hour. The atmosphere is professional -balanced with friendly, caring and relaxed. Our highly qualified staff operate this way to help make your recovery faster and more enjoyable.
------------------------[location: outside, left panel]---------------------------------
The right rehab for your clients
Timely access to comprehensive assessment and treatment
Proven track record in injury rehabilitation
Convenient one-stop service
Customized treatment plans
Integrated, co-ordinated care
Evidence-based care applying leading best practices
Access to specialty clinics: Physiatry and Chronic Pain
-------------------------[location: outside, middle panel]--------------------------
Please call us 416-738-4062
for more information on injury rehabilitation
Vela Motion Group
8120 Tolliver Rd., Unit 9
Scarborough, ON M4K 8B2
[Please include a line art map designed based on "map" file enclosed]
To make a referral for your clients, contact velamotiongroup@brisklane.ca or fax: 416-738-4059. Thank you.
www.velamotiongroup.ca
------------------------------------------------------------------------------------------------
Target Market(s)
family doctors, ER docs, lawyers, and general public age (20-50)
Industry/Entity Type
Health And Wellness
Requirements
Must have
- san serif font
- blue and green colors
- clean, sophisticated look
Nice to have
- consumer choice award badge either on front or back of trifold
Should not have
- see above

```html
<!DOCTYPE html>
<html lang="en">
<head>
<meta charset="utf-8">
<title>Vela Motion – Inside Trifold</title>
<link href="https://fonts.googleapis.com/css2?family=Fira+Sans:ital,wght@0,300;0,400;0,500;0,600;1,300&display=swap" rel="stylesheet">
<style>
  :root {
    --navy: #1a4d89;
    --sky: #6ea5d6;
    --sky-pale: #a9cbe8;
    --paper: #eceef1;
    --lime: #8cc63f;
    --white: #ffffff;
    --ink-blue: #1e4f8c;
    --skin: #e9c3a6;
    --skin-deep: #c99478;
    --seal: #d9a93a;
  }
  * { box-sizing: border-box; margin: 0; padding: 0; }
  html, body { width: 1200px; height: 922px; overflow: hidden; background: var(--white); }
  body { font-family: "Fira Sans", sans-serif; font-weight: 300; }
  .brochure { position: relative; width: 1200px; height: 922px; overflow: hidden; }
  .backdrop, .photo { position: absolute; left: 0; top: 0; }

  .text { position: absolute; color: var(--white); font-size: 14.6px; line-height: 22.4px; text-align: justify; }

  .profile-name { position: absolute; right: 845px; text-align: right; color: var(--white); font-size: 16px; line-height: 22px; }
  .profile-name strong { color: var(--lime); font-weight: 500; font-size: 18px; }
  .profile-name em { display: block; color: var(--lime); font-size: 14px; }

  .services { position: absolute; left: 455px; top: 372px; width: 297px; color: var(--ink-blue); }
  .services h2 { font-size: 30px; font-weight: 500; color: var(--ink-blue); margin-bottom: 10px; }
  .services p { font-size: 14.6px; line-height: 22.4px; text-align: justify; }
  .service-list { list-style: none; margin-top: 8px; }
  .service-list li { font-weight: 500; font-size: 15.5px; line-height: 30px; }
  .service-list li::before { content: "•"; color: var(--lime); margin-right: 6px; }

  .bracing { left: 455px; top: 783px; width: 282px; }

  .brand { position: absolute; left: 905px; top: 42px; width: 160px; text-align: center; color: #d3dbe6; font-size: 22px; font-weight: 500; line-height: 24px; }

  .feature h3 { position: absolute; left: 837px; color: var(--lime); font-size: 20px; font-weight: 500; }
  .feature .text { left: 837px; width: 295px; }
</style>
</head>
<body>
<main class="brochure">
  <svg class="backdrop" width="1200" height="922" viewBox="0 0 1200 922" aria-hidden="true">
    <rect x="0" y="0" width="400" height="922" fill="var(--navy)"/>
    <rect x="395" y="0" width="405" height="922" fill="var(--paper)"/>
    <rect x="795" y="0" width="405" height="922" fill="var(--navy)"/>
    <polygon points="270,0 340,0 430,190 400,190" fill="var(--sky-pale)"/>
    <polygon points="395,0 340,0 400,130" fill="var(--navy)"/>
    <path d="M395,170 L500,335 Q530,365 600,340 L800,275 L800,290 L600,355 Q520,380 490,345 Z" fill="var(--sky)"/>
    <path d="M350,922 L455,760 Q475,735 540,740 L800,768 L800,922 Z" fill="var(--sky)"/>
    <path d="M440,783 Q470,738 540,741 L800,770" fill="none" stroke="var(--navy)" stroke-width="1.5"/>
    <polygon points="395,922 350,922 395,850" fill="var(--navy)"/>
    <rect x="0" y="0" width="20" height="922" fill="var(--lime)"/>
    <rect x="1172" y="0" width="28" height="922" fill="var(--lime)"/>
    <path d="M870,610 Q930,555 1010,585 L1172,640" fill="none" stroke="var(--white)" stroke-width="2"/>
    <path d="M860,630 Q925,565 1010,595 L1172,652" fill="none" stroke="var(--lime)" stroke-width="3"/>
    <path d="M110,40 Q150,30 180,60 L215,100 Q225,115 215,130 L150,275" fill="none" stroke="var(--lime)" stroke-width="2"/>
    <path d="M110,470 Q150,460 180,490 L215,530 Q225,545 215,560 L150,705" fill="none" stroke="var(--lime)" stroke-width="2"/>
    <circle class="award-seal" cx="720" cy="672" r="30" fill="var(--seal)"/>
  </svg>

  <svg class="photo" width="1200" height="922" viewBox="0 0 1200 922" role="img" aria-label="Photo of a physiotherapist adjusting a knee brace on a patient">
    <defs>
      <linearGradient id="kneeTone" x1="0" y1="0" x2="1" y2="1">
        <stop offset="0" stop-color="#dfe9f2"/>
        <stop offset="0.45" stop-color="var(--skin)"/>
        <stop offset="1" stop-color="#f4f4f4"/>
      </linearGradient>
    </defs>
    <path d="M340,0 L800,0 L800,275 L600,340 Q530,362 500,330 L395,165 Z" fill="url(#kneeTone)"/>
  </svg>

  <svg class="photo" width="1200" height="922" viewBox="0 0 1200 922" role="img" aria-label="Photo of hands massaging a patient's back">
    <defs>
      <linearGradient id="backTone" x1="0" y1="0" x2="1" y2="1">
        <stop offset="0" stop-color="#f3d8c3"/>
        <stop offset="0.6" stop-color="var(--skin)"/>
        <stop offset="1" stop-color="var(--skin-deep)"/>
      </linearGradient>
    </defs>
    <path d="M730,922 L860,650 Q925,585 1010,612 L1172,662 L1172,922 Z" fill="url(#backTone)"/>
  </svg>

  <svg class="photo" width="1200" height="922" viewBox="0 0 1200 922" role="img" aria-label="Portrait of Dr. Harriet Osei">
    <defs>
      <linearGradient id="portraitOne" x1="0" y1="0" x2="1" y2="1">
        <stop offset="0" stop-color="#b89a80"/>
        <stop offset="1" stop-color="#eef1f4"/>
      </linearGradient>
    </defs>
    <path d="M0,40 L75,40 Q105,40 125,60 L190,125 Q205,145 190,165 L120,270 Q100,290 75,290 L0,290 Z" fill="url(#portraitOne)"/>
  </svg>

  <svg class="photo" width="1200" height="922" viewBox="0 0 1200 922" role="img" aria-label="Portrait of physiotherapist Dorothy Varga">
    <defs>
      <linearGradient id="portraitTwo" x1="0" y1="0" x2="1" y2="1">
        <stop offset="0" stop-color="#cfd6df"/>
        <stop offset="1" stop-color="#b07a86"/>
      </linearGradient>
    </defs>
    <path d="M0,470 L75,470 Q105,470 125,490 L190,555 Q205,575 190,595 L120,700 Q100,720 75,720 L0,720 Z" fill="url(#portraitTwo)"/>
  </svg>

  <section class="team">
    <p class="profile-name" style="top:227px;"><strong>Harriet Osei,</strong><br>MD, FRCPC, MSC, CIME<em>Physiatrist</em></p>
    <p class="text" style="left:57px; top:304px; width:300px;">Dr. Osei specializes in injury rehab and sports medicine. She is highly trained having received her MD and Residency in Physiatry from Wexmoor University. Her passion is to help injured people get back to their life.</p>
    <p class="profile-name" style="top:684px;"><strong>Dorothy Varga,</strong> PT<em>Physiotherapist</em></p>
    <p class="text" style="left:57px; top:738px; width:298px;">Dorothy has over 10 years of experience as a Physiotherapist (5 in Canada). She has advanced training in orthopedics and manual therapy. She loves and relates well with people form the youngest to the most senior.</p>
  </section>

  <section class="services">
    <h2>Our services</h2>
    <p>We provide integrated assessment and care from interprofessional team of regulated healthcare professionals with proven experience in injury rehabilitation:</p>
    <ul class="service-list">
      <li>physiatrists</li>
      <li>sport medicine physicians</li>
      <li>physiotherapists</li>
      <li>chiropractors</li>
      <li>massage therapists</li>
      <li>acupuncturists</li>
      <li>psychologists</li>
    </ul>
  </section>
  <p class="text bracing">We provide custom medical bracing, orthotics, orthopedic shoes, assistive devices, and medical stockings, all in one place.</p>

  <p class="brand">Vela Motion</p>

  <section class="feature">
    <h3 style="top:107px;">Only registered physiotherapists</h3>
    <p class="text" style="top:143px;">We strongly believe in consistency with your treatment plan. This means that you spend your time here one-on-one with your physiotherapist, not any students or assistants. You get consistent high quality care from a professional.</p>
    <h3 style="top:317px;">One-on-one attention</h3>
    <p class="text" style="top:352px;">We book maximum 3 people per hour to ensure everyone gets adequate one-on-one time with their physiotherapist. This compares favorably with other clinics, who may book upwards of 5-6 per hour. The atmosphere is professional -balanced with friendly, caring and relaxed. Our highly qualified staff operate this way to help make your recovery faster and more enjoyable.</p>
  </section>
</main>
</body>
</html>
```